CREATE A BUSINESS CARD FOR A BOAT CLEANING SERVICE

WE ARE STARTING A NEW BOAT CLEANING BUSINESS. WE DIVE UNDERWATER TO CLEAN BOAT HULLS, JETTIES, UNDERWATER STRUCTURES ETC. WE ARE LOOKING FOR AN UPPERMARKET MODERN LOGO AND BUSINESS CARD AS ALOT OF OUR TARGET MARKET WILL BE HIGH END. YOU HAVE TO DESIGN A BUSINESS CARD AND LOGO SEPERATELY .
THE BUSINESS CARD DIMESNION MUST BE STANDARD SIZE.
The standard dimensions of a printed business card are 3.5 x 2 inches

Target Market(s)

UNDERWATER SERVICED

Industry/Entity Type

Business

Contact Information for Business Card

HALDANE SUBSEA SERVICES

Font styles to use
Serif

Colors

Designer to choose colors to be used in the design.

Requirements
Must have
• HALDANE
Nice to have
• dark
Should not have
• more than 3 colors

```html
<!DOCTYPE html>
<html lang="en">
<head>
<meta charset="utf-8">
<title>Haldane Subsea Services – Business Card</title>
<link rel="stylesheet" href="https://fonts.googleapis.com/css2?family=Roboto:wght@400;500;700&family=Roboto+Condensed:wght@500;700&display=swap">
<style>
  :root {
    --navy: #22337a;
    --paper: #f4f4f3;
    --backdrop: #dedede;
    --ink: #4a4a4a;
    --ink-dark: #1b1b1b;
    --rule: #8a8a8a;
    --white: #ffffff;
  }
  * { margin: 0; padding: 0; box-sizing: border-box; }
  html, body { width: 1200px; height: 960px; overflow: hidden; }
  body {
    position: relative;
    background: var(--backdrop);
    font-family: "Roboto", Arial, sans-serif;
  }
  .card {
    position: absolute;
    width: 600px;
    height: 343px;
    box-shadow: 2px 3px 4px rgba(0,0,0,0.35);
  }
  .card-front { left: 314px; top: 113px; background: var(--paper); }
  .card-back  { left: 311px; top: 472px; background: var(--navy); }

  /* Wordmark (front) */
  .front-brand {
    position: absolute;
    right: 40px;
    top: 90px;
    width: 230px;
    text-align: center;
    color: var(--navy);
    font-weight: 500;
  }
  .front-brand .brand-name { font-size: 40px; line-height: 40px; letter-spacing: 1px; }
  .front-brand .brand-sub { font-size: 11.5px; letter-spacing: 1.2px; margin-top: 6px; }

  /* Name block */
  .name-marker {
    position: absolute; left: 0; top: 177px;
    width: 13px; height: 39px; background: var(--navy);
  }
  .person-name {
    position: absolute; left: 31px; top: 175px;
    font-family: "Roboto Condensed", Arial, sans-serif;
    font-weight: 700; font-size: 23px; color: var(--navy);
  }
  .person-title {
    position: absolute; left: 31px; top: 202px;
    font-size: 14.5px; font-weight: 500; color: var(--ink-dark);
  }
  .divider {
    position: absolute; left: 34px; right: 34px; top: 228px;
    height: 1px; background: var(--rule);
  }

  /* Contacts */
  .contact-list { position: absolute; left: 33px; top: 241px; list-style: none; }
  .contact-list li {
    display: flex; align-items: center; height: 19px;
    font-size: 14.5px; color: var(--ink);
  }
  .contact-list svg { width: 13px; height: 13px; margin-right: 9px; fill: var(--navy); flex: none; }
  .address {
    position: absolute; right: 34px; top: 263px;
    text-align: right; font-size: 14.5px; line-height: 18px; color: var(--ink);
    font-style: normal;
  }

  /* Back */
  .back-brand {
    position: absolute; left: 0; right: 0; top: 155px;
    text-align: center; color: var(--white); font-weight: 500;
  }
  .back-brand .brand-name { font-size: 48px; line-height: 46px; letter-spacing: 1.5px; }
  .back-brand .brand-sub { font-size: 14px; letter-spacing: 1.4px; margin-top: 6px; }
  .web-band {
    position: absolute; left: 0; right: 0; top: 286px; height: 27px;
    background: var(--paper);
    display: flex; align-items: center; justify-content: center;
    font-size: 15px; letter-spacing: 3px; color: var(--ink);
  }
</style>
</head>
<body>

<section class="card card-front" aria-label="Business card front">
  <div class="front-brand">
    <div class="brand-name">HALDANE</div>
    <div class="brand-sub">SUBSEA SERVICES</div>
  </div>

  <div class="name-marker"></div>
  <h1 class="person-name">ELLIOT MARSH</h1>
  <p class="person-title">CEO/FOUNDER</p>
  <div class="divider"></div>

  <ul class="contact-list">
    <li>
      <svg viewBox="0 0 24 24" aria-hidden="true"><path d="M6.6 10.8c1.4 2.8 3.8 5.1 6.6 6.6l2.2-2.2c.3-.3.7-.4 1-.2 1.1.4 2.3.6 3.6.6.6 0 1 .4 1 1V20c0 .6-.4 1-1 1C10.6 21 3 13.4 3 4c0-.6.4-1 1-1h3.5c.6 0 1 .4 1 1 0 1.3.2 2.5.6 3.6.1.3 0 .7-.2 1L6.6 10.8z"/></svg>
      614 552 7031
    </li>
    <li>
      <svg viewBox="0 0 24 24" aria-hidden="true"><path d="M7 1h10a2 2 0 0 1 2 2v18a2 2 0 0 1-2 2H7a2 2 0 0 1-2-2V3a2 2 0 0 1 2-2zm0 3v15h10V4H7zm5 16.2a1 1 0 1 0 0 .1z"/></svg>
      728 305 4419
    </li>
    <li>
      <svg viewBox="0 0 24 24" aria-hidden="true"><path d="M6 2h12v5H6zM3 8h18a2 2 0 0 1 2 2v7h-4v5H5v-5H1v-7a2 2 0 0 1 2-2zm4 8v4h10v-4H7z"/></svg>
      593 210 8675
    </li>
    <li>
      <svg viewBox="0 0 24 24" aria-hidden="true"><path d="M2 5h20v14H2zm2 2v.4l8 5 8-5V7H4z"/></svg>
      elliot@haldane.com
    </li>
  </ul>

  <address class="address">
    2146 Harbor View Road<br>
    Anchorage, Alaska 34512<br>
    www.haldane.com
  </address>
</section>

<section class="card card-back" aria-label="Business card back">
  <div class="back-brand">
    <div class="brand-name">HALDANE</div>
    <div class="brand-sub">SUBSEA SERVICES</div>
  </div>
  <div class="web-band">www.haldanesubseaservices.com</div>
</section>

</body>
</html>
```